Halvex Consulting

Hi,
I have my own network consulting business (just me)
and need to get a logo and business card design together,

Based in New Zealand,

Gareth Pollard
Unified Communications and Network Architect

/design engineer,
and would like this to be the basis for personal branding and company identity

Reason: I will be off site for a couple of days - so you have some more time

Business

• I have the basis for a optional logo - needs color -

```html
<!DOCTYPE html>
<html lang="en">
<head>
<meta charset="utf-8">
<title>Halvex Consulting — Business Card</title>
<link rel="stylesheet" href="https://fonts.googleapis.com/css2?family=Open+Sans:wght@300;400;700&display=swap">
<style>
  :root {
    --backdrop: #e4e4e4;
    --card: #231f20;
    --text: #ffffff;
    --text-soft: #e9e9e9;
    --rule: #5a5657;
    --accent: #3f8fe0;
  }
  * { margin: 0; padding: 0; box-sizing: border-box; }
  html, body {
    width: 1200px;
    height: 822px;
    overflow: hidden;
    background: var(--backdrop);
    font-family: "Open Sans", Arial, sans-serif;
  }
  .business-card {
    position: absolute;
    left: 40px;
    top: 100px;
    width: 1120px;
    height: 622px;
    background: var(--card);
    color: var(--text);
  }
  .brand {
    position: absolute;
    left: 58px;
    top: 50px;
    display: flex;
    align-items: flex-end;
    gap: 10px;
  }
  .brand-dot {
    width: 92px;
    height: 92px;
    border-radius: 50%;
    background: var(--accent);
  }
  .brand-name {
    font-weight: 700;
    font-size: 34px;
    letter-spacing: 0.5px;
    line-height: 1;
    text-transform: uppercase;
    padding-bottom: 2px;
  }
  .person {
    position: absolute;
    left: 163px;
    top: 330px;
  }
  .person-name {
    font-weight: 400;
    font-size: 50px;
    line-height: 1.2;
    margin-bottom: 8px;
  }
  .person-role {
    font-size: 25px;
    line-height: 38px;
    color: var(--text-soft);
  }
  .divider {
    position: absolute;
    left: 622px;
    top: 342px;
    width: 2px;
    height: 188px;
    background: var(--rule);
  }
  .contact-list {
    position: absolute;
    left: 650px;
    top: 330px;
    list-style: none;
    font-size: 26px;
    line-height: 38px;
    color: var(--text-soft);
  }
  .contact-item {
    display: flex;
    align-items: flex-start;
  }
  .contact-icon {
    width: 40px;
    height: 38px;
    flex: none;
    display: flex;
    align-items: center;
    justify-content: flex-start;
    color: var(--text);
  }
  .contact-icon svg { width: 30px; height: 26px; fill: currentColor; }
  .contact-icon.at { font-weight: 700; font-size: 30px; }
  .contact-text { padding-left: 14px; }
</style>
</head>
<body>
  <section class="business-card">
    <div class="brand">
      <span class="brand-dot"></span>
      <span class="brand-name">Halvex Consulting</span>
    </div>

    <div class="person">
      <h1 class="person-name">Gareth Pollard</h1>
      <p class="person-role">Unified Communications<br>and Network Architect<br>Design engineer</p>
    </div>

    <div class="divider"></div>

    <ul class="contact-list">
      <li class="contact-item">
        <span class="contact-icon">
          <svg viewBox="0 0 30 22"><path d="M0 0h30v22H0z" fill="none"/><path d="M1 1h28v20H1z M3 3v1.2l12 8.2 12-8.2V3z M3 7v12h24V7L15 15.2z" fill-rule="evenodd"/></svg>
        </span>
        <span class="contact-text">4512, Kauri Ridge Rd,<br>New Zealand</span>
      </li>
      <li class="contact-item">
        <span class="contact-icon">
          <svg viewBox="0 0 30 26"><path d="M2 9c0-4 6-7 13-7s13 3 13 7v2h-7V8c-2-1-4-1.4-6-1.4S11 7 9 8v3H2z"/><path d="M8 12h14l4 12H4z"/><circle cx="15" cy="18" r="3" fill="#231f20"/></svg>
        </span>
        <span class="contact-text">310 555 0142</span>
      </li>
      <li class="contact-item">
        <span class="contact-icon">
          <svg viewBox="0 0 30 26"><path d="M8 1h14v7H8z"/><path d="M2 9h26v11h-5v-4H7v4H2z"/><path d="M8 17h14v8H8z"/></svg>
        </span>
        <span class="contact-text">087 555 0199</span>
      </li>
      <li class="contact-item">
        <span class="contact-icon at">@</span>
        <span class="contact-text">inbox@halvex.com</span>
      </li>
    </ul>
  </section>
</body>
</html>
```